The Wisdom of Lanterns New Book Cover Design Project

Book cover design . Paperback, ebook, and Talvora (derived from book cover) files/images required.
Book Title: The Wisdom of Lanterns
Subtitle: Under Copper Bridges
Author: Daniel Forsythe
Files: Ebook, Paperback (Brindlewick & Halvern Quill), Talvora sized image
File size & information to be provided once design is ready. Brindlewick paperback will be 5.25 x 8.
Completion date is flexible. Planning to publish in November.
Updates

Target Market(s)

Motorcycle owners

Font styles to use
Sans Serif

Requirements
Must have
• A generic looking motorcycle (samples attached). Thumbnail easily recognized as a motorcycle book.
Nice to have
• Open to all ideas but am favoring my idea: to emphasize the title lettering similar to (but not a copy of) other Wisdom books (examples attached), on a plain background. All books in the category have a motorcycle on the cover. Author name and subtitle do not have to be prominent. Rider optional..
Should not have
• Should not look like a biker romance or fantasy cover or look cartoonish. Motorcycle pic should be fairly generic (brand, style,).

```html
<!DOCTYPE html>
<html lang="en">
<head>
<meta charset="utf-8">
<title>The Wisdom of Lanterns — Cover</title>
<link rel="stylesheet" href="https://fonts.googleapis.com/css2?family=Josefin+Sans:wght@400;600&family=Playfair+Display:wght@500;700&display=swap">
<style>
  :root {
    --page-bg: #ffffff;
    --cover-bg: #ffffff;
    --ink: #1b1b1b;
    --accent: #ff3c0a;
    --bike-dark: #2a2a2a;
    --bike-mid: #8a8a88;
    --bike-light: #e9e9e7;
  }
  * { margin: 0; padding: 0; box-sizing: border-box; }
  html, body {
    width: 1200px;
    height: 381px;
    overflow: hidden;
    background: var(--page-bg);
  }
  .stage {
    position: relative;
    width: 1200px;
    height: 381px;
    display: flex;
    justify-content: center;
    align-items: center;
  }
  .cover {
    position: relative;
    width: 250px;
    height: 381px;
    background: var(--cover-bg);
  }
  .cover__subtitle {
    position: absolute;
    top: 22px;
    left: 0;
    width: 100%;
    text-align: center;
    font-family: "Josefin Sans", sans-serif;
    font-weight: 400;
    font-size: 11.5px;
    letter-spacing: 2.2px;
    color: var(--ink);
    text-transform: uppercase;
  }
  .cover__title {
    position: absolute;
    top: 0;
    left: 0;
    width: 250px;
    height: 381px;
  }
  .cover__title text {
    font-family: "Playfair Display", serif;
  }
  .title__main { fill: var(--accent); font-weight: 500; }
  .title__small { fill: var(--ink); font-weight: 700; }
  .cover__art {
    position: absolute;
    left: 48px;
    top: 214px;
    width: 158px;
    height: 118px;
    border-radius: 50% 50% 8px 8px / 40% 40% 8px 8px;
    background: radial-gradient(ellipse at 50% 55%, var(--bike-dark) 0%, var(--bike-mid) 55%, var(--bike-light) 85%, var(--cover-bg) 100%);
  }
  .cover__author {
    position: absolute;
    top: 344px;
    left: 0;
    width: 100%;
    text-align: center;
    font-family: "Josefin Sans", sans-serif;
    font-weight: 400;
    font-size: 18px;
    letter-spacing: 2.6px;
    color: var(--accent);
    text-transform: uppercase;
  }
</style>
</head>
<body>
  <main class="stage">
    <section class="cover">
      <p class="cover__subtitle">Under Copper Bridges</p>

      <svg class="cover__title" viewBox="0 0 250 381" aria-label="The Wisdom of Lanterns">
        <text class="title__main" x="70" y="168" font-size="122" textLength="172" lengthAdjust="spacingAndGlyphs">Wisdom</text>
        <text class="title__small" x="30" y="166" font-size="40" textLength="36" lengthAdjust="spacingAndGlyphs">The</text>
        <text class="title__small" x="8" y="204" font-size="42" textLength="150" lengthAdjust="spacingAndGlyphs">of Lanterns</text>
      </svg>

      <div class="cover__art" role="img" aria-label="Photograph of a classic black motorcycle seen from the front three-quarter angle"></div>

      <p class="cover__author">Daniel Forsythe</p>
    </section>
  </main>
</body>
</html>
```